Professional Financial services company want to rebrand their stationary

We need stationary design for Velmor Group, its a company with 4 member companys that include Velmor Auditing, Velmor Financial Consultancy, Velmor Debt Collection and Velmor Real Estate.

We are based in dubai so the designers need to keep in mind that we use both english and arabic so leave a space for the arabic writing.

We recently redesigned our Logo and would like to redesign our stationary to go along with it.

You will find attached the logo, please keep it looking professional and use the logo as a guide for colors when designing.

Good luck to everyone

Industry/Entity Type

Finance And Accounting

Font styles to use
Sans Serif

Colors
0292cd
33a6d7
3276b5
0355a3
ffffff
dbdbdb

Requirements
Must have
• Letterhead
• Business card
• Envelope small and A4
Nice to have
• Professional
• Space for Arabic and english

```html
<!DOCTYPE html>
<html lang="en">
<head>
<meta charset="utf-8">
<title>Velmor Group — Business Card</title>
<link rel="stylesheet" href="https://fonts.googleapis.com/css2?family=Montserrat:wght@600&family=Roboto:wght@400;500;700&family=Roboto+Condensed:wght@700&family=Noto+Naskh+Arabic:wght@400;700&display=swap">
<style>
  :root {
    --brand-blue: #0a6ebd;
    --card-black: #1c1d1f;
    --card-white: #f4f4f4;
    --text-grey: #555555;
    --backdrop: #d2d2d2;
    --white: #ffffff;
  }
  * { margin: 0; padding: 0; box-sizing: border-box; }
  html, body { width: 1200px; height: 960px; overflow: hidden; }
  body {
    background: var(--backdrop);
    font-family: "Roboto", Arial, sans-serif;
    position: relative;
  }
  .card { position: absolute; }

  /* Back of card */
  .card-back {
    left: 322px; top: 107px; width: 606px; height: 348px;
    background: var(--card-black);
  }
  .back-mark {
    position: absolute; left: 223px; top: 83px; width: 155px; height: 155px;
    border: 10px solid var(--brand-blue);
  }
  .members-title {
    position: absolute; left: 0; right: 0; top: 259px; text-align: center;
    color: var(--brand-blue); font-weight: 500; font-size: 14px; letter-spacing: 0.2px;
  }
  .members-list {
    position: absolute; left: 0; right: 0; top: 284px; text-align: center;
    color: var(--white); font-size: 14.5px; line-height: 20px;
  }
  .members-list .dot {
    display: inline-block; width: 7px; height: 7px; border-radius: 50%;
    background: var(--brand-blue); margin: 0 6px; vertical-align: middle; position: relative; top: -1px;
  }

  /* Front of card */
  .card-front {
    left: 320px; top: 493px; width: 601px; height: 345px;
    background: var(--brand-blue); padding: 12px;
  }
  .front-inner {
    position: relative; width: 100%; height: 100%;
    background: var(--card-white);
  }
  .brand {
    position: absolute; left: 24px; top: 22px; display: flex; align-items: center; gap: 14px;
  }
  .brand-square { width: 44px; height: 44px; border: 4px solid var(--brand-blue); }
  .brand-name {
    font-family: "Montserrat", Arial, sans-serif; font-weight: 600; font-size: 29px;
    color: var(--brand-blue); letter-spacing: -0.3px;
  }
  .person { position: absolute; right: 25px; top: 128px; display: flex; gap: 14px; }
  .person-ar { text-align: right; font-family: "Noto Naskh Arabic", serif; direction: rtl; }
  .person-ar .name-ar { color: var(--brand-blue); font-weight: 700; font-size: 25px; line-height: 30px; }
  .person-ar .title-ar { color: var(--text-grey); font-size: 18px; line-height: 20px; text-align: left; }
  .person-en { text-align: right; font-family: "Roboto Condensed", Arial, sans-serif; }
  .person-en .name-en { color: var(--brand-blue); font-weight: 700; font-size: 21px; line-height: 26px; margin-top: 6px; }
  .person-en .title-en { color: var(--text-grey); font-weight: 700; font-size: 15px; line-height: 22px; }

  .address { position: absolute; left: 23px; top: 206px; color: var(--text-grey); font-size: 14.5px; line-height: 19px; }
  .address-ar { margin-top: 6px; font-family: "Noto Naskh Arabic", serif; direction: rtl; text-align: left; unicode-bidi: plaintext; line-height: 23px; font-size: 14px; }
  .address-ar p { direction: rtl; text-align: right; }

  .contacts { position: absolute; right: 25px; top: 205px; list-style: none; color: var(--text-grey); font-size: 14.5px; }
  .contacts li { display: flex; justify-content: flex-end; align-items: center; gap: 8px; height: 19px; }
  .contacts svg { width: 13px; height: 13px; fill: var(--brand-blue); }
</style>
</head>
<body>

<section class="card card-back" aria-label="Business card back">
  <div class="back-mark"></div>
  <h2 class="members-title">MEMBER COMPANIES</h2>
  <div class="members-list">
    <p>Velmor Auditing<span class="dot"></span>Velmor Financial Consultancy</p>
    <p>Velmor Debt Collection<span class="dot"></span>Velmor Real Estate</p>
  </div>
</section>

<section class="card card-front" aria-label="Business card front">
  <div class="front-inner">
    <div class="brand">
      <div class="brand-square"></div>
      <span class="brand-name">VELMOR GROUP</span>
    </div>

    <div class="person">
      <div class="person-ar" lang="ar">
        <p class="name-ar">كريم حداد</p>
        <p class="title-ar">مؤسس</p>
      </div>
      <div class="person-en">
        <p class="name-en">KARIM HADDAD</p>
        <p class="title-en">CEO/FOUNDER</p>
      </div>
    </div>

    <div class="address">
      <p>4219 Cedar Court</p>
      <p>Fairbanks, Alaska 61803</p>
      <div class="address-ar" lang="ar">
        <p style="text-align:left">4219 سيدار كورت</p>
        <p style="text-align:left">فيربانكس، ألاسكا 61803</p>
      </div>
    </div>

    <ul class="contacts">
      <li>512 774 3081
        <svg viewBox="0 0 16 16" aria-hidden="true"><path d="M3.5 1l2.5 3-1.5 1.8c.9 2 2.6 3.7 4.7 4.7L11 9l3 2.5-1.3 2.7C7 14 2 9 1.8 3.2z"/></svg></li>
      <li>947 205 6613
        <svg viewBox="0 0 16 16" aria-hidden="true"><path d="M4 0h8v16H4zM5.5 2v10h5V2zM7 13.2h2v1.3H7z" fill-rule="evenodd"/></svg></li>
      <li>318 560 2749
        <svg viewBox="0 0 16 16" aria-hidden="true"><path d="M4 1h8v4H4zM1 6h14v6h-2v3H3v-3H1zM4.5 10v3.5h7V10z" fill-rule="evenodd"/></svg></li>
      <li>name@velmorgroup.com
        <svg viewBox="0 0 16 16" aria-hidden="true"><path d="M1 3h14v1.5L8 9 1 4.5zM1 6.3l7 4.5 7-4.5V13H1z"/></svg></li>
      <li>www.velmorgroup.com
        <svg viewBox="0 0 16 16" aria-hidden="true"><circle cx="8" cy="8" r="7"/></svg></li>
    </ul>
  </div>
</section>

</body>
</html>
```